Cosmetic injections clinic needs a fresh looking business card

We need a business card using the supplied logo and color scheme to attract future clients to our clinic. It should be modern and fresh, eye catching and not too busy. Simple and to the point is best. I would like two sided designs with the front indicating address and contact information, and the back in full color with white logo and descriptive information also provided.
Target Market(s)
Clients looking for non surgical beauty enhancements.
Contact Information for Business Card
Lumivela
14, 415 Carrow Ridge Road
Marlow Bay, Northland
K2P 7W3
Phone: 431-662-0974
Email: info@lumivela-example.com
Requirements
Must have
- -Logo supplied with the name and address of the clinic
- -Back of card in full color with white logo with A small line of text indicating both of the following: Anti aging consultants and cosmetic injectables
- Located inside the Wayfarer Care Group

```html
<!DOCTYPE html>
<html lang="en">
<head>
<meta charset="utf-8">
<title>Lumivela Business Card</title>
<link rel="stylesheet" href="https://fonts.googleapis.com/css2?family=Lato:wght@300;400;700&family=Raleway:wght@300;400&display=swap">
<style>
  :root {
    --bg: #ecebee;
    --card-white: #ffffff;
    --brand-pink: #e2449a;
    --brand-purple: #6a3d9a;
    --brand-teal: #23b9a6;
    --ink: #111111;
    --rule: #7a7a7a;
    --shadow: 0 10px 28px rgba(0,0,0,0.18);
  }
  * { box-sizing: border-box; margin: 0; padding: 0; }
  html, body {
    width: 1200px; height: 994px; overflow: hidden;
    background: var(--bg);
    font-family: "Lato", sans-serif;
  }
  .stage { position: relative; width: 1200px; height: 994px; }

  .card {
    position: absolute;
    width: 600px; height: 343px;
    box-shadow: var(--shadow);
    overflow: hidden;
  }

  /* Back of card */
  .card--back {
    left: 540px; top: 110px;
    background: var(--brand-pink);
    color: #ffffff;
  }
  .card--back .brand {
    position: absolute; left: 0; right: 0; top: 110px;
    display: flex; align-items: center; justify-content: center; gap: 16px;
  }
  .card--back .brand-dot {
    width: 40px; height: 40px; border-radius: 50%; background: #ffffff;
  }
  .card--back .brand-name {
    font-weight: 700; font-size: 56px; letter-spacing: 1px; color: #ffffff;
  }
  .tagline {
    position: absolute; left: 0; right: 0; top: 200px;
    text-align: center;
    font-family: "Raleway", sans-serif; font-weight: 300;
    font-size: 19px; letter-spacing: 0.5px;
  }

  /* Front of card */
  .card--front {
    left: 60px; top: 540px;
    background: var(--card-white);
    color: var(--ink);
  }
  .card--front .brand {
    position: absolute; left: 36px; top: 34px;
    display: flex; align-items: center; gap: 12px;
  }
  .card--front .brand-dot {
    width: 30px; height: 30px; border-radius: 50%; background: var(--brand-purple);
  }
  .card--front .brand-name {
    font-weight: 700; font-size: 40px; color: var(--brand-pink); letter-spacing: 0.5px;
  }
  .rule-top {
    position: absolute; left: 36px; right: 0; top: 112px;
    border-top: 1.5px solid var(--rule);
  }
  .contact {
    position: absolute; right: 40px; top: 128px;
    text-align: right;
  }
  .contact .clinic-name {
    font-size: 34px; font-weight: 400; line-height: 1.2; margin-bottom: 6px;
  }
  .contact-line {
    display: flex; align-items: center; justify-content: flex-end; gap: 10px;
    font-size: 17px; line-height: 26px;
  }
  .contact-line svg { width: 20px; height: 20px; }
  .rule-mid {
    position: absolute; left: 250px; right: 40px; top: 246px;
    border-top: 1.5px solid var(--rule);
  }
  .address {
    position: absolute; right: 40px; top: 254px;
    text-align: right; font-size: 17px; line-height: 24px; font-style: normal;
  }
  .accent-band {
    position: absolute; left: 150px; right: 0; bottom: 0; height: 30px;
    background: var(--brand-teal);
    border-top-left-radius: 26px;
  }
</style>
</head>
<body>
<main class="stage">

  <section class="card card--back" aria-label="Back of business card">
    <div class="brand">
      <span class="brand-dot"></span>
      <span class="brand-name">Lumivela</span>
    </div>
    <p class="tagline">Anti aging consultants and cosmetic injectables</p>
  </section>

  <section class="card card--front" aria-label="Front of business card">
    <div class="brand">
      <span class="brand-dot"></span>
      <span class="brand-name">Lumivela</span>
    </div>
    <div class="rule-top"></div>

    <div class="contact">
      <h1 class="clinic-name">Lumivela</h1>
      <p class="contact-line">431-662-0974 :
        <svg viewBox="0 0 20 20" aria-hidden="true">
          <circle cx="10" cy="10" r="8.5" fill="none" stroke="#111" stroke-width="1.6"/>
          <path d="M7 6.5c.8-.6 1.4-.4 1.7.4l.4 1.1c.2.5 0 .9-.4 1.2.5 1 1.2 1.7 2.1 2.1.3-.4.7-.6 1.2-.4l1.1.4c.8.3 1 .9.4 1.7-1.4 1.6-6.9-3.1-6.5-6.5z" fill="#111"/>
        </svg>
      </p>
      <p class="contact-line">info@lumivela-example.com :
        <svg viewBox="0 0 20 20" aria-hidden="true">
          <rect x="2" y="5" width="16" height="11" fill="#111"/>
          <path d="M2.5 5.5 10 11.5 17.5 5.5M2.5 15.5 8 10.5M17.5 15.5 12 10.5" fill="none" stroke="#fff" stroke-width="1.2"/>
        </svg>
      </p>
    </div>
    <div class="rule-mid"></div>

    <address class="address">
      14, 415 Carrow Ridge Road<br>
      Marlow Bay, Northland, K2P 7W3
    </address>

    <div class="accent-band"></div>
  </section>

</main>
</body>
</html>
```